Lone Star Wetland Flora Stewardship Guild

We need to design the home page of this new website. We would like a fun website design for provides as a resource for members and information for potential members.
Please design so that we can see a portion of background on each side on the website.
I just need the final design files psd no coding needed.
Attached is their logo (colors are not 100% set in stone either so can mess with those as I did in the quick mockup attached)
Attached is a pdf newsletter they send out, you can get a feel for them and what they are about. The design is crappy and we are here to fix that going forward and we are starting with the website.
Here are some quick example websites (design style is open)
- I attached a quick mockup i did just for a content visual but by all means do what you want.
- http://www.brindlecourtleaders.org/
- http://www.qvelto.org/
- http://preview.plimworks7.com/view.php?cat=layoutpacks&host=gridcrafthub&temp=venrolite
- http://www.ploughvale.org/
- http://www.townmarrow.org/
- http://www.projectkindlecoat.org/
here are some of the other chapters website (pretty bad!)
and here are some of the others:
- http://www.zrelkq.org/
- http://ovtu.org/
- http://www.lirvx.org/
Content Items that need to be included:
1. Logo
2. Menu - home, about, members, resources, events, membership, contact
3. Become a member - button or action
4. social links - friendwall, jobrungo, clipzora
5. banner - that needs to explain their purpose "Promoting environmental stewardship through operations, research, education and outreach" (or this can be worked into the design)
6. Upcoming event (s)
7. Advertisement - members can place an ad on the website, this can be a placeholder for now
8. newsletter signup
9. advertise with us - this link can be in the footer
30-60 years of age, succesfull (household budgets of 120K+ men and women that live in texas.
Education

```html
<!DOCTYPE html>
<html lang="en">
<head>
<meta charset="utf-8">
<title>Lone Star Wetland Flora Stewardship Guild</title>
<link href="https://fonts.googleapis.com/css2?family=Open+Sans:wght@400;600;700&display=swap" rel="stylesheet">
<style>
:root{
  --navy:#1d3f8a;
  --red:#d04452;
  --red-dark:#b62d3b;
  --text:#555;
  --muted:#777;
  --footer:#3d3f44;
  --footer-dark:#2b2d31;
  --blue:#3a97e8;
  --white:#fff;
}
*{margin:0;padding:0;box-sizing:border-box}
html,body{width:882px;height:1200px;overflow:hidden;background:var(--white)}
body{position:relative;font-family:"Open Sans",Arial,sans-serif;color:var(--text)}
.abs{position:absolute}

/* header */
.brand{left:80px;top:58px;width:290px;color:var(--navy);font-weight:700;font-size:22px;line-height:28px}
.socials{left:573px;top:53px;display:flex;gap:8px}
.socials span{width:27px;height:27px;border:2px solid var(--navy);border-radius:50%;display:block}
.util{top:58px;font-size:11px;color:#444;display:flex;align-items:center;gap:6px}
.util.login{left:685px}
.util.contact{left:745px;padding-left:8px;border-left:1px solid #ddd}
.btn-member{left:690px;top:105px;width:112px;height:30px;background:linear-gradient(#5a5b5e,#333438);color:#fff;font-size:11.5px;border-radius:3px;display:flex;align-items:center;justify-content:center}

/* nav */
.nav{left:0;top:182px;width:882px;height:36px;background:linear-gradient(#dc5563,var(--red-dark));border-top:1px solid #e9808a}
.nav ul{list-style:none;position:absolute;left:80px;top:0;display:flex;height:36px}
.nav li{height:36px;display:flex;align-items:center;justify-content:center;color:#fff;font-size:12px;border-right:1px solid rgba(0,0,0,.12)}
.nav li:last-child{border-right:none}
.nav li.active{background:rgba(0,0,0,.12)}

/* hero */
.hero{left:0;top:218px;width:882px;height:470px;overflow:hidden}
.hero-photo{position:absolute;inset:0;background:linear-gradient(180deg,#f2f5ee 0%,#a8c86a 30%,#6d9a3c 48%,#8aa86a 62%,#5f7f4c 78%,#7b8c5a 100%)}
.hero-caption{position:absolute;left:146px;top:232px;width:481px;height:79px;background:rgba(60,70,70,.55);color:#fff;font-size:16.5px;line-height:28px;padding:10px 16px;text-transform:uppercase}
.hero-arrow{position:absolute;top:195px}

/* content */
.h2{font-size:19px;color:var(--navy);font-weight:400;letter-spacing:-.3px}
.about-title{left:80px;top:734px}
.about-text{left:80px;top:768px;width:218px;font-size:9px;line-height:15.5px;color:var(--muted)}
.about-text p+p{margin-top:6px}
.events-title{left:345px;top:734px}
.event{left:345px;width:220px;height:50px}
.event-thumb{position:absolute;left:0;top:0;width:67px;height:46px;border:3px solid #fff;box-shadow:0 0 2px rgba(0,0,0,.35);background:linear-gradient(#cfe0ea,#6a9a58 55%,#3f6e45)}
.event-title{position:absolute;left:77px;top:3px;font-size:9px;color:var(--red);white-space:nowrap}
.event-text{position:absolute;left:77px;top:18px;font-size:8.5px;line-height:15px;color:var(--muted);width:140px}
.ad{left:596px;top:738px;width:206px;height:206px;background:linear-gradient(#1a1b22 0%,#2a2c36 70%,#d9d9d9 72%,#e4e4e4 100%)}
.ad-name{position:absolute;left:0;right:0;bottom:14px;text-align:center;color:#1e2a4a;font-weight:700;font-size:16px}

/* footer */
.footer{left:0;top:987px;width:882px;height:167px;background:linear-gradient(var(--footer),#36383c)}
.footer-h{font-size:13px;color:#fff;font-weight:400}
.footer-list{list-style:none;font-size:9px;line-height:18px;color:#eee}
.contact-row{display:flex;gap:9px;align-items:flex-start;font-size:9px;color:#eee;line-height:17px}
.contact-row svg{flex:none;margin-top:3px}
.foot-social{display:flex;gap:6px}
.foot-social span{width:18px;height:18px;border-radius:50%;background:#fff;display:block}
.news-input{left:632px;top:1081px;width:166px;height:21px;background:#fff;border:1px solid #ccc}
.subscribe{left:723px;top:1113px;width:74px;height:23px;background:var(--blue);color:#fff;font-size:10px;display:flex;align-items:center;justify-content:center}
.copyright{left:0;top:1154px;width:882px;height:46px;background:var(--footer-dark);border-top:1px solid #4a4c50;color:#ddd;font-size:8.5px;padding:16px 0 0 81px}
</style>
</head>
<body>

<header>
  <div class="abs brand">Lone Star Wetland Flora<br>Stewardship Guild</div>
  <div class="abs socials" aria-label="Social links: friendwall, clipzora, jobrungo">
    <span title="friendwall"></span><span title="clipzora"></span><span title="jobrungo"></span>
  </div>
  <div class="abs util login">
    <svg width="8" height="10" viewBox="0 0 8 10"><rect x="0" y="4" width="8" height="6" fill="#444"/><path d="M2 4V2.5a2 2 0 0 1 4 0V4" stroke="#444" stroke-width="1.3" fill="none"/></svg>Login
  </div>
  <div class="abs util contact">
    <svg width="11" height="9" viewBox="0 0 11 9"><rect x=".5" y=".5" width="10" height="8" fill="none" stroke="#444"/><path d="M.5 .5l5 4 5-4" fill="none" stroke="#444"/></svg>Contact
  </div>
  <div class="abs btn-member">Become a Member</div>
</header>

<nav class="abs nav">
  <ul>
    <li class="active" style="width:75px">HOME</li>
    <li style="width:113px">ABOUT US</li>
    <li style="width:102px">MEMBERS</li>
    <li style="width:119px">RESOURCES</li>
    <li style="width:93px">EVENTS</li>
    <li style="width:119px">MEMBERSHIP</li>
    <li style="width:101px">CONTACT</li>
  </ul>
</nav>

<section class="abs hero">
  <div class="hero-photo" role="img" aria-label="Photo of a calm wetland pond framed by tall reeds and green trees reflected in the water"></div>
  <svg class="hero-arrow" style="left:86px" width="14" height="22" viewBox="0 0 14 22"><path d="M10 3L3 11l7 8" stroke="#fff" stroke-width="1.5" fill="none" opacity=".8"/></svg>
  <svg class="hero-arrow" style="left:780px" width="14" height="22" viewBox="0 0 14 22"><path d="M4 3l7 8-7 8" stroke="#fff" stroke-width="1.5" fill="none" opacity=".8"/></svg>
  <div class="hero-caption">Promoting environmental stewardship through operations, research, education and outreach</div>
  <svg style="position:absolute;left:0;bottom:0" width="882" height="72" viewBox="0 0 882 72" preserveAspectRatio="none"><path d="M0 40 C180 80 380 80 560 40 C680 12 790 8 882 20 L882 72 L0 72Z" fill="#fff"/></svg>
</section>

<main>
  <h2 class="abs h2 about-title">About Us</h2>
  <div class="abs about-text">
    <p>Claritas est etiam processus dynamicus, qui sequitur mutationem consuetudium lectorum. Mirum est notare quam littera gothica, quam nunc putamus parum claram, anteposuerit litterarum formas humanitatis per seacula quarta decima et quinta decima. Eodem modo typi, qui nunc nobis videntur parum clari, fiant sollemnes in futurum.</p>
    <p>Duis autem vel eum iriure dolor in hendrerit in vulputate velit esse molestie consequat, vel illum dolore eu feugiat nulla facilisis Claritas est etiam processus dynamicus, qui sequitur mutationem consuetudium lectorum. Mirum est notare quam littera gothica, quam nunc putamus.</p>
  </div>

  <h2 class="abs h2 events-title">Upcoming Events</h2>
  <div class="abs event" style="top:772px">
    <div class="event-thumb" role="img" aria-label="Event photo of lily pads on a pond"></div>
    <div class="event-title">Duis autem vel eum iriure dolor</div>
    <div class="event-text">Brianne craves the endorphin rufueled by fitness and uses it.</div>
  </div>
  <div class="abs event" style="top:832px">
    <div class="event-thumb" role="img" aria-label="Event photo of a marsh under blue sky"></div>
    <div class="event-title">Duis autem vel eum iriure dolor</div>
    <div class="event-text">Brianne craves the endorphin rufueled by fitness and uses it.</div>
  </div>
  <div class="abs event" style="top:893px">
    <div class="event-thumb" role="img" aria-label="Event photo of flowering water lilies"></div>
    <div class="event-title">Duis autem vel eum iriure dolor</div>
    <div class="event-text">Brianne craves the endorphin rufueled by fitness and uses it.</div>
  </div>

  <div class="abs ad" role="img" aria-label="Member advertisement: product photo of an algae treatment container">
    <div class="ad-name">Reedmark Labs</div>
  </div>
</main>

<footer>
  <div class="abs footer"></div>
  <h3 class="abs footer-h" style="left:80px;top:1015px">Advertise with us</h3>
  <ul class="abs footer-list" style="left:81px;top:1039px">
    <li>Duis autem vel</li><li>Eodem modo typi</li><li>validations and verification</li><li>System monitoring</li><li>Emergency Breakdowns</li>
  </ul>

  <h3 class="abs footer-h" style="left:255px;top:1015px">Contact Us</h3>
  <div class="abs" style="left:254px;top:1040px">
    <div class="contact-row"><svg width="8" height="11" viewBox="0 0 8 11"><path d="M4 11C1 7 0 5.5 0 4a4 4 0 0 1 8 0c0 1.5-1 3-4 7z" fill="#ccc"/><circle cx="4" cy="4" r="1.4" fill="#3d3f44"/></svg><span style="padding-left:5px">2400 Marsh Hollow Rd.<br>Austin TX 78701</span></div>
    <div class="contact-row" style="margin-top:2px"><svg width="11" height="8" viewBox="0 0 11 8"><rect width="11" height="8" fill="#ccc"/><path d="M0 0l5.5 4.5L11 0" stroke="#3d3f44" fill="none"/></svg><span>info@wetlandguild.org</span></div>
    <div class="contact-row" style="margin-top:4px"><svg width="10" height="10" viewBox="0 0 10 10"><path d="M2 0l2 2.5-1.2 1.3a6 6 0 0 0 3.4 3.4L7.5 6 10 8 8.5 10C4 9.5.5 6 0 1.5z" fill="#ccc"/></svg><span style="color:#bbb">51 204 7731</span></div>
  </div>

  <h3 class="abs footer-h" style="left:440px;top:1015px">Follow Us</h3>
  <p class="abs" style="left:441px;top:1042px;width:140px;font-size:9px;line-height:17px;color:#eee">Follow us our news and events through social networks.</p>
  <div class="abs foot-social" style="left:441px;top:1085px" aria-label="Social network links"><span></span><span></span><span></span><span></span></div>

  <h3 class="abs footer-h" style="left:632px;top:1015px">Newsletter</h3>
  <p class="abs" style="left:632px;top:1040px;width:175px;font-size:9px;line-height:17px;color:#eee">Stay in touch with us by signing up for our quarterly newsletter!</p>
  <div class="abs news-input"></div>
  <div class="abs subscribe">SUBSCRIBE</div>

  <div class="abs copyright">Copyright ©2013. All Rights Reserved.</div>
</footer>

</body>
</html>
```